Veradine Contracting Folder

Creating a design for the cover of our folders that we pass to our customers

Want to keep the same look as our colors and fonts as attached

```html
<!DOCTYPE html>
<html lang="en">
<head>
<meta charset="utf-8">
<title>Veradine Contracting Folder</title>
<link href="https://fonts.googleapis.com/css2?family=Questrial&display=swap" rel="stylesheet">
<style>
  :root{
    --bg:#e4e4e4;
    --navy:#1a1d9e;
    --blue:#2b2fb3;
    --blue-light:#4548bd;
    --lavender:#a3a3d6;
    --yellow:#e1bc2b;
    --white:#f4f4f4;
    --label:#333;
    --sky-top:#3f9ad6;
    --sky-soft:#a9cbe3;
  }
  *{box-sizing:border-box;margin:0;padding:0}
  html,body{width:1200px;height:1200px;overflow:hidden;background:var(--bg);font-family:"Questrial",sans-serif}
  .stage{position:relative;width:1200px;height:1200px}
  .panel{position:absolute;overflow:hidden;box-shadow:0 6px 18px rgba(0,0,0,.12)}
  .block,.photo{position:absolute}
  .label{position:absolute;font-size:20px;letter-spacing:5px;color:var(--label);display:flex;align-items:center;gap:18px}
  .label::before{content:"";width:90px;height:1px;background:var(--label)}

  /* front */
  .front{left:80px;top:60px;width:380px;height:492px;background:var(--white)}
  .b-blue{background:var(--navy)}
  .b-yellow{background:var(--yellow)}
  .b-lav{background:var(--lavender)}
  .ph-skyline{background:linear-gradient(180deg,#e8e3e6,#c9b7b8)}
  .ph-tools{background:linear-gradient(135deg,#eeeeee 0%,#f0d64a 40%,#e9e9e9 75%)}
  .ph-sky{background:linear-gradient(180deg,var(--sky-top),#d6e9f5)}
  .ph-painter{background:linear-gradient(135deg,#b8393c 0%,#d9d9d9 55%,#c4463e 100%)}
  .wordmark{position:absolute;display:flex;align-items:center;gap:8px;font-size:40px;letter-spacing:3px;line-height:1;white-space:nowrap}
  .wordmark .mark{width:10px;height:10px;background:var(--yellow)}
  .front .wordmark{left:95px;top:372px;color:var(--navy)}
  .tagline{position:absolute;font-size:15px;letter-spacing:4px;white-space:nowrap}
  .front .tagline{left:86px;top:424px;color:var(--lavender)}

  /* back */
  .back{left:740px;top:60px;width:380px;height:492px;background:linear-gradient(135deg,var(--navy) 0%,var(--blue) 60%,var(--blue-light) 100%)}
  .ph-site-left{background:linear-gradient(90deg,#f0e3a8,#d9c06a)}
  .ph-site-right{background:linear-gradient(90deg,#8a9a8c,#cdd3cf)}
  .back .wordmark{left:96px;top:218px;color:#fff;font-size:32px}
  .back .tagline{left:96px;top:262px;color:#fff;font-size:13px}
  .contact{position:absolute;right:40px;bottom:44px;color:#fff;font-size:9px;line-height:1.5;letter-spacing:1px;text-align:right;font-style:normal}

  /* inside */
  .inside{left:220px;top:640px;width:760px;height:492px;background:var(--sky-soft)}
  .ph-buildings{left:0;top:0;width:760px;height:492px;background:linear-gradient(180deg,var(--sky-top) 0%,var(--sky-soft) 100%)}
  .fold{position:absolute;left:379px;top:0;width:2px;height:492px;background:rgba(255,255,255,.35)}
  .pocket{position:absolute;left:0;top:0}

  .label-front{left:100px;top:572px}
  .label-back{left:760px;top:572px}
  .label-inside{left:470px;top:1148px}
</style>
</head>
<body>
<main class="stage">

  <section class="panel front" aria-label="Front cover">
    <div class="photo ph-skyline" style="left:0;top:0;width:240px;height:50px" role="img" aria-label="City skyline photo"></div>
    <div class="block b-blue" style="left:248px;top:0;width:132px;height:44px"></div>
    <div class="block b-yellow" style="left:0;top:56px;width:40px;height:150px"></div>
    <div class="photo ph-tools" style="left:46px;top:56px;width:334px;height:112px" role="img" aria-label="Yellow hard hat, level and safety glasses on blueprints"></div>
    <div class="photo ph-sky" style="left:46px;top:174px;width:164px;height:76px" role="img" aria-label="Blue sky with clouds"></div>
    <div class="block b-lav" style="left:250px;top:174px;width:130px;height:32px"></div>
    <div class="photo ph-painter" style="left:216px;top:212px;width:164px;height:88px" role="img" aria-label="Painter on scaffolding at a red building"></div>
    <div class="block b-blue" style="left:0;top:256px;width:210px;height:64px"></div>
    <div class="wordmark"><span class="mark"></span>VERADINE</div>
    <p class="tagline">Painting &amp; Contracting</p>
  </section>

  <section class="panel back" aria-label="Back cover">
    <div class="photo ph-site-left" style="left:0;top:222px;width:86px;height:34px" role="img" aria-label="Construction site at sunset"></div>
    <div class="photo ph-site-right" style="left:330px;top:208px;width:50px;height:34px" role="img" aria-label="Construction site with cranes"></div>
    <div class="wordmark"><span class="mark"></span>VERADINE</div>
    <p class="tagline">Painting &amp; Consulting</p>
    <address class="contact">www.veradine.com<br>info@veradine.com<br>+1 (555) 014 2290</address>
  </section>

  <section class="panel inside" aria-label="Inside spread">
    <div class="photo ph-buildings" role="img" aria-label="Modern glass office towers with trees under blue sky"></div>
    <div class="fold"></div>
    <svg class="pocket" width="760" height="492" viewBox="0 0 760 492">
      <path d="M760 0 H620 Q560 0 560 60 V320 H760 Z" fill="var(--lavender)"/>
      <path d="M500 492 V380 A120 120 0 0 1 620 260 H760 V492 Z" fill="var(--yellow)"/>
    </svg>
  </section>

  <p class="label label-front">FRONT</p>
  <p class="label label-back">BACK</p>
  <p class="label label-inside">INSIDE</p>

</main>
</body>
</html>
```